Web Design for Small Healthcare Startup

Hello,

We are seeking a Website Design for a healthcare company focusing on mobile vaccinations, employee health and wellness services onsite at businesses, and consulting services relating to Healthcare Entities in WA state. Our company’s mission is to “To aid in a healthier workplace”. Brightpath Rovers will provide on-site wellness services to employers that simplify and streamline employee preventative health as well as onsite consulting services to help with compliance of Healthcare Entities.

We are seeking a Website Design for Brightpath Rovers, PLLC. Our company’s mission is to provide mobile health and wellness services to employers onsite at their businesses. These services include mobile vaccinations clinics for employees as well as wellness and health screenings. The company will also offer healtcare compliance consulting services for Healthcare Entities. The company was founded to bring these important healthcare services to businesses and keep employees healthy. Healthy employees are the cornerstone to a great business and we want to help orginazations achieve their goals of having a healthy productive workforce.

We are looking for a moderin website design that will need to be coded. We have attached our current logo design for reference as well as a brief questionare regarding our business for your information (not necessary to include all information). We would like something SEO friendly and easy to navigate.

Thank you!

Brightpath Rovers, PLLC

Target Market(s)

Small Businesses

Industry/Entity Type

Healthcare

Coding

Coded - Design and coding required

Number of Pages Required

1 page

Requirements
Nice to have
• SEO Friendly, Incorporate Logo

```html
<!DOCTYPE html>
<html lang="en">
<head>
<meta charset="utf-8">
<title>Brightpath Rovers, PLLC – To Aid In A Healthier Workplace</title>
<meta name="viewport" content="width=1200">
<link href="https://fonts.googleapis.com/css2?family=Lato:wght@400;700;900&display=swap" rel="stylesheet">
<style>
:root{
  --navy:#06224a;
  --navy-deep:#041a3a;
  --blue:#1d4fa8;
  --magenta:#c956c6;
  --magenta-deep:#a53a9c;
  --pink-btn:#cc4fc5;
  --text:#2a2a2a;
  --muted:#444;
  --white:#fff;
}
*{box-sizing:border-box;margin:0;padding:0}
html,body{width:1200px;height:4129px;overflow:hidden}
body{font-family:'Lato',sans-serif;color:var(--text);background:#fff;position:relative}
.abs{position:absolute}
.btn{position:absolute;display:flex;align-items:center;justify-content:center;background:var(--pink-btn);color:#fff;font-size:14px;border-radius:22px;text-decoration:none;white-space:nowrap}

/* header */
.site-header{position:absolute;top:0;left:0;width:1200px;height:67px;background:#fff;z-index:5}
.brand{position:absolute;left:72px;top:22px;display:flex;align-items:center;gap:8px;font-weight:700;font-size:17px;color:var(--blue)}
.brand-dot{width:14px;height:14px;border-radius:50%;background:var(--magenta)}
.main-nav{position:absolute;left:442px;top:25px;font-size:13px}
.main-nav a{color:#333;text-decoration:none;position:absolute;white-space:nowrap}
.main-nav a.active{color:var(--blue);font-weight:700}
.nav-underline{position:absolute;left:436px;top:48px;width:42px;height:3px;background:var(--magenta)}
.phone-head{position:absolute;left:971px;top:17px;display:flex;align-items:center;gap:13px}
.phone-dot{width:33px;height:33px;border-radius:50%;background:linear-gradient(135deg,#7fa8f0,#c07ee0);display:flex;align-items:center;justify-content:center;flex:none}
.phone-head small{display:block;font-size:12px;font-weight:700;color:#222}
.phone-head strong{display:block;font-size:17px;color:#222}

/* hero */
.hero{position:absolute;top:67px;left:0;width:1200px;height:570px;overflow:hidden}
.hero-bg{position:absolute;inset:0;background:linear-gradient(100deg,#2f6ed8 0%,#6a62d6 35%,#c45bd8 65%,#e456c8 100%);border-bottom-right-radius:420px 300px}
.hero h1{position:absolute;top:120px;left:0;width:1200px;text-align:center;color:#fff;font-size:76px;font-weight:900;line-height:84px}
.hero p{position:absolute;top:302px;left:0;width:1200px;text-align:center;color:#fff;font-size:29px;line-height:40px}
.hero .btn{left:540px;top:403px;width:118px;height:41px}
.bar{position:absolute;height:14px}

/* sections */
.blob-photo{position:absolute;background:linear-gradient(135deg,#a88f7a,#5e5a8a 55%,#3a3f70);box-shadow:0 8px 20px rgba(0,0,0,.18)}
h2.sec{position:absolute;font-size:38px;font-weight:700;line-height:52px;color:#222}
p.body{position:absolute;font-size:13.5px;line-height:23px;color:var(--muted)}

.why{position:absolute;top:1163px;left:0;width:1200px;height:733px;background:var(--navy)}
.why h2{position:absolute;top:60px;width:1200px;text-align:center;color:#fff;font-size:37px;font-weight:700}
.card{position:absolute;top:135px;width:337px;height:483px;background:linear-gradient(180deg,#1d3f8e 0%,#3a3e9a 40%,#6b3ea8 70%);overflow:hidden;border-bottom-left-radius:110px}
.card p{position:absolute;top:40px;left:28px;right:28px;text-align:center;color:#fff;font-weight:700;font-size:17.5px;line-height:26px}
.card .photo{position:absolute;left:0;bottom:0;width:337px;height:315px;clip-path:polygon(0 0,100% 18%,100% 100%,0 100%)}
.card .icon{position:absolute;right:28px;top:208px;width:82px;height:82px;border-radius:50%;background:var(--navy);border:5px solid #fff;display:flex;align-items:center;justify-content:center}

.flu{position:absolute;top:2355px;left:0;width:1200px;height:423px;background:radial-gradient(ellipse at 30% 60%,#2a5fc8,#1542a8 60%,#0f3a9a)}
.flu h2{position:absolute;top:130px;width:1200px;text-align:center;color:#fff;font-size:38px;font-weight:700}
.flu p{position:absolute;top:187px;width:1200px;text-align:center;color:#fff;font-size:26px}
.flu .btn{left:541px;top:243px;width:118px;height:41px}

.reserve{position:absolute;top:3305px;left:0;width:1200px;height:483px;background:linear-gradient(90deg,#2f63d8 0%,#6d5ad6 45%,#c456d8 80%,#de55cc 100%);border-top-left-radius:380px 140px}
.reserve h2{position:absolute;top:38px;width:1200px;text-align:center;color:#fff;font-size:38px;font-weight:700;line-height:51px}
.field{position:absolute;height:46px;background:#fff;font-size:13px;color:#222;padding:0 18px;display:flex;align-items:center;justify-content:space-between}
.reserve .btn{left:458px;top:353px;width:283px;height:42px}
.reserve .call{position:absolute;top:416px;width:1200px;text-align:center;color:#fff;font-size:15px;text-decoration:underline}

.site-footer{position:absolute;top:3788px;left:0;width:1200px;height:300px;background:var(--navy-deep)}
.foot-brand{position:absolute;top:92px;width:1200px;text-align:center;color:#fff;font-weight:700;font-size:26px}
.foot-contact{position:absolute;top:170px;width:1200px;display:flex;justify-content:center;gap:30px;color:#fff;font-size:17px}
.foot-contact span{display:flex;align-items:center;gap:14px}
.foot-nav{position:absolute;top:232px;width:1200px;display:flex;justify-content:center;gap:45px;font-size:14px}
.foot-nav a{color:#fff;text-decoration:none}
.copyright{position:absolute;top:4088px;left:0;width:1200px;height:41px;background:#03142d;color:#fff;font-size:12px;display:flex;align-items:center;justify-content:center}
</style>
</head>
<body>

<header class="site-header">
  <div class="brand"><span class="brand-dot"></span>Brightpath Rovers</div>
  <nav class="main-nav">
    <a class="active" href="#" style="left:0">Home</a>
    <a href="#" style="left:78px">About</a>
    <a href="#" style="left:156px">Services</a>
    <a href="#" style="left:248px">Schedule</a>
    <a href="#" style="left:344px">Pricing</a>
    <a href="#" style="left:427px">Contact</a>
  </nav>
  <div class="nav-underline"></div>
  <div class="phone-head">
    <span class="phone-dot"><svg width="15" height="15" viewBox="0 0 24 24"><path fill="#fff" d="M6.6 10.8a15 15 0 0 0 6.6 6.6l2.2-2.2c.3-.3.7-.4 1-.2 1.1.4 2.3.6 3.6.6.6 0 1 .4 1 1V20c0 .6-.4 1-1 1A17 17 0 0 1 3 4c0-.6.4-1 1-1h3.5c.6 0 1 .4 1 1 0 1.3.2 2.5.6 3.6.1.3 0 .7-.2 1z"/></svg></span>
    <div><small>Phone:</small><strong>555-014-2270</strong></div>
  </div>
</header>

<section class="hero">
  <div class="hero-bg" role="img" aria-label="Gloved hand giving a vaccine injection, tinted blue to magenta"></div>
  <h1>To Aid In A Healthier<br>Workplace</h1>
  <p>We offer healtcare compliance consulting services for<br>Healthcare Entities.</p>
  <a class="btn" href="#">Contact Us</a>
</section>
<div class="bar" style="top:622px;left:0;width:722px;background:#1a4aa0"></div>
<div class="bar" style="top:636px;left:94px;width:726px;background:var(--magenta-deep)"></div>

<section>
  <div class="blob-photo" role="img" aria-label="Pharmacist vaccinating a seated man in a pharmacy" style="left:76px;top:700px;width:325px;height:420px;border-radius:55% 45% 50% 50% / 45% 50% 50% 55%"></div>
  <div class="abs" style="left:256px;top:880px;width:290px;height:240px;background:#fff;border-radius:60% 40% 45% 55% / 50% 40% 60% 50%"></div>
  <h2 class="sec" style="left:611px;top:770px">Making The Workplace A<br>Healthier Place</h2>
  <p class="body" style="left:611px;top:888px;width:520px">It is a long established fact that a reader will be distracted by the readable content of a page when looking at its layout.Many desktop publishing packages and web page editors .</p>
  <a class="btn" href="#" style="left:611px;top:980px;width:269px;height:41px">Vaccination Rates And Production</a>
</section>

<section class="why">
  <h2>Why Choose Us</h2>
  <div class="card" style="left:71px">
    <p>Brightpath Rovers specializes in providing seamless, hassle-free, on-site mobile vaccine clinics.</p>
    <div class="photo" role="img" aria-label="Health worker in a mask preparing a syringe" style="background:linear-gradient(135deg,#d9d4cc,#8a7f78)"></div>
    <div class="icon"><svg width="36" height="36" viewBox="0 0 24 24" fill="none" stroke="#fff" stroke-width="1.6"><path d="M4 20l9-9M10 8l6 6M14 4l6 6M17 7l-2-2"/></svg></div>
  </div>
  <div class="card" style="left:431px">
    <p>No crowded waiting rooms, no long lines, no hassle!</p>
    <div class="photo" role="img" aria-label="Civil protection worker checking forms with a masked woman" style="background:linear-gradient(135deg,#c96a3a,#2c3e70)"></div>
    <div class="icon"><svg width="36" height="36" viewBox="0 0 24 24" fill="none" stroke="#fff" stroke-width="1.6"><path d="M5 12l4 4 10-10"/></svg></div>
  </div>
  <div class="card" style="left:791px">
    <p>Specializing in workplace employee vaccine clinics. Great service to offer as part of your company's Employee Wellness Package.</p>
    <div class="photo" role="img" aria-label="Doctor vaccinating a masked woman at her desk" style="background:linear-gradient(135deg,#e8e6e2,#6f6a62)"></div>
    <div class="icon"><svg width="38" height="38" viewBox="0 0 24 24" fill="none" stroke="#fff" stroke-width="1.5"><circle cx="12" cy="8" r="3"/><circle cx="5" cy="10" r="2"/><circle cx="19" cy="10" r="2"/><path d="M6 19c0-3 3-5 6-5s6 2 6 5M1 18c0-2 2-3 4-3M23 18c0-2-2-3-4-3"/></svg></div>
  </div>
</section>

<section>
  <h2 class="sec" style="left:72px;top:1993px">Offering Flu and Covid<br>Vaccinations</h2>
  <p class="body" style="left:72px;top:2113px;width:445px">It is a long established fact that a reader will be distracted by the readable content of a page when looking at its layout.Many desktop publishing packages and web page editors .</p>
  <a class="btn" href="#" style="left:72px;top:2205px;width:120px;height:43px">Contact Us</a>
  <div class="abs" style="left:687px;top:1958px;width:442px;height:338px;background:var(--magenta);border-radius:0 30px 30px 0"></div>
  <div class="abs" role="img" aria-label="Vaccine vial and syringe on a yellow background" style="left:664px;top:1980px;width:449px;height:296px;background:linear-gradient(135deg,#f0d562,#e4bd3e);border-radius:0 30px 30px 0"></div>
</section>

<section class="flu" role="img" aria-label="Patient receiving a flu shot, tinted blue">
  <h2>RHB Flu Shot Recommendations</h2>
  <p>(Yearly Flu Shot Between Aug -Dec?)</p>
  <a class="btn" href="#">Read More</a>
</section>

<section>
  <div class="blob-photo" role="img" aria-label="Smiling businesswoman holding a face mask in an office" style="left:72px;top:2818px;width:463px;height:415px;border-radius:40% 60% 55% 45% / 45% 55% 45% 55%;background:linear-gradient(135deg,#cfd8e2,#55606e)"></div>
  <h2 class="sec" style="left:613px;top:2890px">Avoid Long Lines</h2>
  <p class="body" style="left:613px;top:2960px;width:470px">Each employee can sign up for specific time or dept managers can release employees in phases to clinic. Also available: book for entire day so employees can get vaccinated as their workload permits.<br>Employees will avoid congested waiting rooms at medical offices and long lines at local pharmacies</p>
  <a class="btn" href="#" style="left:613px;top:3106px;width:118px;height:43px">Contact Us</a>
</section>

<div class="bar" style="top:3290px;left:378px;width:727px;height:13px;background:var(--magenta-deep)"></div>
<div class="bar" style="top:3303px;left:475px;width:725px;height:13px;background:#1a4aa0"></div>
<section class="reserve">
  <h2>Reserve Your On-site Mobile<br>Vaccine Clinic Today!</h2>
  <div class="field" style="left:287px;top:167px;width:307px">Business Name</div>
  <div class="field" style="left:605px;top:167px;width:307px">Location</div>
  <div class="field" style="left:287px;top:227px;width:625px">Contact Person Info</div>
  <div class="field" style="left:287px;top:285px;width:307px">Employees/vaccines</div>
  <div class="field" style="left:605px;top:285px;width:307px">Time<svg width="12" height="8" viewBox="0 0 12 8"><path d="M1 1l5 5 5-5" fill="none" stroke="#222" stroke-width="1.5"/></svg></div>
  <a class="btn" href="#">Show Calender For Available Dates</a>
  <a class="call" href="#">or call directly for more information</a>
</section>

<footer class="site-footer">
  <div class="foot-brand">Brightpath Rovers</div>
  <div class="foot-contact">
    <span><span class="phone-dot"><svg width="15" height="15" viewBox="0 0 24 24"><path fill="#fff" d="M6.6 10.8a15 15 0 0 0 6.6 6.6l2.2-2.2c.3-.3.7-.4 1-.2 1.1.4 2.3.6 3.6.6.6 0 1 .4 1 1V20c0 .6-.4 1-1 1A17 17 0 0 1 3 4c0-.6.4-1 1-1h3.5c.6 0 1 .4 1 1 0 1.3.2 2.5.6 3.6.1.3 0 .7-.2 1z"/></svg></span>Phone:&nbsp; 555-014-2270</span>
    <span><span class="phone-dot"><svg width="15" height="15" viewBox="0 0 24 24"><path fill="#fff" d="M3 6h18v12H3z"/><path d="M3 6l9 7 9-7" fill="none" stroke="#a47ee0" stroke-width="1.5"/></svg></span>Email:&nbsp; hello@brightpathrovers.example</span>
  </div>
  <nav class="foot-nav">
    <a href="#">Home</a><a href="#">About</a><a href="#">Services</a><a href="#">Schedule</a><a href="#">Pricing</a><a href="#">Contact</a>
  </nav>
</footer>
<div class="copyright">Copyright © 2022 Brightpath Rovers,All Right Reserved</div>

</body>
</html>
```